Sing Across The Harbor redesign book cover

A new cover for my already published book. The old cover looks great but not for a women’s self help book. Cover is killing sales. Once I explain the book it sells quickly AND gets 5 star reviews. Outside of actually explaining the book the cover scares people away. I need a new cover. ASAP! Before The yr end please.
The tag line -
Discover 10 Practical Ways To Replace negative thoughts with knowing the voice of God. This is a self help book for women 35-45 Christian but not religious. Each chapter is a hands on spiritual experience where the reader takes small tests about themselves, discover why they have negative thoughts, what they are and how to listen to God through hands on methods of listening. NOT strange type of things. They learn what 4 voices they are listening to and how to hone in on Jesus voice. There are scriptures to pray and journaling assignments. The old cover is in the brief with the write up for the back of the book. Please use the new author picture, Publishers logo (tree), barcode, and contact info from the back of the book. And yes the author name and title of the book on the spine. Lay out on the back cover needs to be interesting. You have all the info have fun with it.

Target Market(s)

Women 35-45 yrs old Christian and new believers or seekers.

Industry/Entity Type

Non profit organization. Missionary

Requirements
Must have
• Something DIFFERENT than what is there now. Something inviting. Fresh clear title
Nice to have
• Multi colors however a white stand out cover is also good.
Should not have
• Heavy religious feeling. No church steeples, Jesus faces.

```html
<!DOCTYPE html>
<html lang="en">
<head>
<meta charset="utf-8">
<title>Sing Across The Harbor – Cover</title>
<link rel="stylesheet" href="https://fonts.googleapis.com/css2?family=Cinzel+Decorative:wght@400;700&family=Cinzel:wght@400&family=Crimson+Text:ital@1&display=swap">
<style>
  :root {
    --sky-deep: #8e1c2a;
    --sky-red: #d9352e;
    --sky-orange: #ef6a2a;
    --sky-glow: #ffd36a;
    --sea: #5a2a3e;
    --gold-light: #d99a22;
    --gold-dark: #c0730f;
    --barcode-box: #fdfce4;
    --rule: #c9962e;
    --white: #ffffff;
  }
  * { margin: 0; padding: 0; box-sizing: border-box; }
  html, body { width: 1200px; height: 877px; overflow: hidden; background: #ffffff; }
  .cover { position: relative; width: 1200px; height: 877px; overflow: hidden; }

  .sky {
    position: absolute; left: 0; top: 0; width: 1200px; height: 782px;
    background:
      radial-gradient(ellipse 220px 160px at 755px 640px, rgba(255,230,140,.95), rgba(255,160,60,0) 70%),
      radial-gradient(ellipse 500px 260px at 420px 520px, rgba(255,120,40,.55), rgba(255,120,40,0) 70%),
      linear-gradient(180deg, var(--sky-deep) 0%, var(--sky-red) 30%, var(--sky-orange) 62%, #a04a50 80%, var(--sea) 100%);
  }
  .back-band {
    position: absolute; left: 0; top: 622px; width: 584px; height: 255px;
    background: linear-gradient(180deg, var(--gold-light), var(--gold-dark));
  }
  .front-band {
    position: absolute; left: 586px; top: 782px; width: 614px; height: 95px;
    background: linear-gradient(180deg, var(--gold-light), var(--gold-dark));
  }
  .barcode-box {
    position: absolute; left: 364px; top: 736px; width: 196px; height: 116px;
    background: var(--barcode-box);
  }

  .title {
    position: absolute; color: var(--white);
    font-family: "Cinzel Decorative", "Cinzel", serif; font-weight: 400;
    text-align: center; line-height: 1.05;
    text-shadow: 0 2px 4px rgba(60,0,0,.45);
  }
  .title .small { font-size: .55em; }
  .back-title { left: 40px; top: 78px; width: 500px; font-size: 40px; }
  .front-title { left: 612px; top: 40px; width: 588px; font-size: 62px; }

  .back-blurb {
    position: absolute; left: 38px; top: 283px; width: 498px;
    font-family: "Crimson Text", Georgia, serif; font-style: italic;
    font-size: 13.6px; line-height: 17.8px; color: var(--white); text-align: center;
  }

  .spine-text {
    position: absolute; writing-mode: vertical-rl; color: var(--white);
    font-family: "Cinzel", serif; font-size: 19px; letter-spacing: .5px;
  }
  .spine-title { left: 587px; top: 46px; }
  .spine-author { left: 587px; top: 572px; }

  .divider { position: absolute; left: 664px; top: 257px; }
  .tagline {
    position: absolute; left: 640px; top: 282px; width: 540px;
    font-family: "Crimson Text", Georgia, serif; font-style: italic;
    font-size: 21.5px; line-height: 29px; color: var(--white); text-align: center;
  }
  .author {
    position: absolute; left: 612px; top: 800px; width: 588px; text-align: center;
    font-family: "Cinzel", serif; font-size: 44px; color: var(--white); letter-spacing: 1px;
  }
</style>
</head>
<body>
<main class="cover">
  <div class="sky" role="img" aria-label="Photograph of a fiery red and orange sunset sky over distant mountains and water, with a woman seen from behind raising her arms wide toward the setting sun"></div>
  <div class="back-band"></div>
  <div class="front-band"></div>
  <div class="barcode-box"></div>

  <h2 class="title back-title">Sing Across<br><span class="small">the</span> Harbor</h2>
  <p class="back-blurb">This is a self help book for women 35-45 Christian but not religious. Each chapter is a hands on spiritual experience where the reader takes small tests about themselves, discover why they have negative thoughts, what they are and how to listen to God through hands on methods of listening. NOT strange type of things. They learn what 4 voices they are listening to and how to hone in on Jesus voice. There are scriptures to pray and journaling assignments.</p>

  <div class="spine-text spine-title">SING ACROSS THE HARBOR</div>
  <div class="spine-text spine-author">MARLA FENNICK</div>

  <h1 class="title front-title">Sing Across<br><span class="small">the</span> Harbor</h1>
  <svg class="divider" width="456" height="14" viewBox="0 0 456 14" aria-hidden="true">
    <polygon points="0,7 200,5.5 228,7 200,8.5" fill="var(--rule)"/>
    <polygon points="456,7 256,5.5 228,7 256,8.5" fill="var(--rule)"/>
    <circle cx="228" cy="7" r="6.5" fill="var(--rule)"/>
  </svg>
  <p class="tagline">Discover 10 Practical Ways To Replace negative thoughts with knowing the voice of God.</p>
  <p class="author">Marla Fennick</p>
</main>
</body>
</html>
```